Wealth Education Business Needs Sharp Business Card Design

We need a business card design for a recently launched investor education business called Harbor Crest.

The final design should promote security, empowerment, self improvement and financial gain. The card will ideally promote the stature of the business.

For more information and colours please visit harborcrest.com.au

Target Market(s)

Corporate executives and high net worth individuals

Industry/Entity Type

Education

Contact Information for Business Card

Name
Position
Contact Address
Phone
Mobile
Email
Website

```html
<!DOCTYPE html>
<html lang="en">
<head>
<meta charset="utf-8">
<title>Harbor Crest Business Card</title>
<link rel="stylesheet" href="https://fonts.googleapis.com/css2?family=Saira:wght@400;500&family=Saira+Condensed:wght@400&display=swap">
<style>
  :root {
    --page: #c9ccd1;
    --card-light: #f4f4f4;
    --card-shade: #dcdcdc;
    --charcoal: #3f3c3d;
    --teal: #1a7479;
    --ink: #3a3a3a;
    --muted: #4a4a4a;
    --white: #ffffff;
  }
  * { box-sizing: border-box; margin: 0; padding: 0; }
  html, body { width: 1200px; height: 866px; overflow: hidden; }
  body {
    background: var(--page);
    font-family: "Saira", sans-serif;
    position: relative;
  }
  .card {
    position: absolute;
    top: 278px;
    width: 540px;
    height: 310px;
    background: radial-gradient(ellipse at 55% 45%, var(--white) 0%, var(--card-light) 45%, var(--card-shade) 100%);
    box-shadow: 0 10px 24px rgba(0,0,0,0.18);
    overflow: hidden;
  }
  .card--front { left: 40px; }
  .card--back { left: 620px; }

  .brand {
    display: flex;
    align-items: center;
    gap: 12px;
    white-space: nowrap;
  }
  .brand__mark {
    flex: none;
    width: 22px; height: 22px;
    background: var(--teal);
  }
  .brand__name {
    font-family: "Saira Condensed", sans-serif;
    font-weight: 400;
    color: var(--ink);
    letter-spacing: 0.14em;
    text-transform: uppercase;
    line-height: 1.2;
  }
  .card--front .brand {
    position: absolute;
    left: 50%; top: 50%;
    transform: translate(-50%, -50%);
  }
  .card--front .brand__name { font-size: 40px; }

  .back-shapes { position: absolute; inset: 0; width: 100%; height: 100%; }
  .card--back .brand { position: absolute; left: 34px; top: 92px; }
  .card--back .brand__mark { width: 16px; height: 16px; }
  .card--back .brand__name { font-size: 27px; }

  .holder {
    position: absolute;
    right: 26px; top: 26px;
    text-align: right;
    line-height: 1.3;
  }
  .holder__name {
    color: var(--teal);
    font-size: 19px;
    font-weight: 500;
    letter-spacing: 0.05em;
  }
  .holder__role {
    color: var(--muted);
    font-size: 13px;
  }

  .address {
    position: absolute;
    right: 26px; top: 162px;
    text-align: right;
    color: var(--white);
    font-size: 12px;
    line-height: 1.45;
  }
  .website {
    position: absolute;
    right: 26px; top: 216px;
    color: var(--white);
    font-size: 12.5px;
  }

  .contacts {
    position: absolute;
    left: 30px; bottom: 16px;
    list-style: none;
    color: var(--white);
    font-size: 11.5px;
  }
  .contacts li {
    display: flex;
    align-items: center;
    gap: 9px;
    height: 18px;
  }
  .contacts svg { width: 11px; height: 11px; fill: var(--white); }
</style>
</head>
<body>

<section class="card card--front" aria-label="Card front">
  <div class="brand">
    <span class="brand__mark"></span>
    <span class="brand__name">Harbor Crest</span>
  </div>
</section>

<section class="card card--back" aria-label="Card back">
  <svg class="back-shapes" viewBox="0 0 540 310" preserveAspectRatio="none" aria-hidden="true">
    <path d="M0,214 C170,190 360,140 540,108 L540,310 L0,310 Z" fill="#3f3c3d"/>
    <path d="M0,192 C170,170 360,118 500,88 C360,128 170,182 0,204 Z" fill="#1a7479"/>
  </svg>

  <div class="brand">
    <span class="brand__mark"></span>
    <span class="brand__name">Harbor Crest</span>
  </div>

  <div class="holder">
    <p class="holder__name">DANIEL MORROW</p>
    <p class="holder__role">Managing Director</p>
  </div>

  <p class="address">12 Quay Street, Level 18<br>Sydney NSW</p>
  <p class="website">www.harborcrest.com.au</p>

  <ul class="contacts">
    <li><svg viewBox="0 0 24 24"><path d="M6.6 10.8a15 15 0 0 0 6.6 6.6l2.2-2.2a1 1 0 0 1 1-.25 11 11 0 0 0 3.6.6 1 1 0 0 1 1 1V20a1 1 0 0 1-1 1A17 17 0 0 1 3 4a1 1 0 0 1 1-1h3.5a1 1 0 0 1 1 1 11 11 0 0 0 .6 3.6 1 1 0 0 1-.25 1z"/></svg>012 345 6789</li>
    <li><svg viewBox="0 0 24 24"><path d="M7 1h10a2 2 0 0 1 2 2v18a2 2 0 0 1-2 2H7a2 2 0 0 1-2-2V3a2 2 0 0 1 2-2zm0 3v14h10V4z"/></svg>012 345 6789</li>
    <li><svg viewBox="0 0 24 24"><path d="M6 2h9v5h3v5h2v10H4V12h2zm2 2v8h8V9h-3V4zM7 15v2h2v-2zm4 0v2h2v-2zm4 0v2h2v-2z"/></svg>012 345 6789</li>
    <li><svg viewBox="0 0 24 24"><path d="M2 5h20v14H2zm2 2v.5l8 5 8-5V7zm0 3v7h16v-7l-8 5z"/></svg>daniel@harborcrest.com.au</li>
  </ul>
</section>

</body>
</html>
```